Swimming Pool Service Website needed!!!

Hi Everyone! Thanks for looking at my contest. I PROMISE to provide excellent feedback during this process.

I am starting a new swimming pool business cleaning company in San Diego, California and would like your help in making it similar to one of these two websites that are already functioning.

http://www.brightlagoonworks.example/services-repair.html

http://tidemarkaquacare.example/commercial-pool-cleaning.php

I like these two because they are easy to read, classy, sophisticated and have nice pictures of really clean & clear pools.

I really like the blue on white color format.

I do not have a logo, but the name of my company is GLIMMERWAVE POOL SERVICE.

My tag line is: Water so pure, it sparkles like a summer sky. (does not need to have the quotes around "in"...maybe just italics for this word IN?) You decide for me.

I would like to have a logo designed that incorporates some sort of easy to read letters. I do not want cursive (handwriting) letters. I thought about having a "reflection" of letters (mirror image), but think that this will be hard to read from far away. Maybe you can surprise me and come up with an idea that works using the a mirror image....but I'm not sure. I was leaning toward plain old BLOCK letters as I think it would be easy to read on my truck.

I would like to have 5 pages on my website:
1) Home
2) About Us (Know Your Poolman) / Why Hire Us
3) Services Offered
4) FAQ's
5) Contact

I am looking for a fully-functioning website (coded). Upon selection of the design winner, I am offering to increase the budget/payment by $100-$125 for the coding of all the pages. So anyone looking at participating in this contest, should be willing and able to provide the coding to the webpages that i've requested.

Target Market(s)

Upper middle-class homeowners who have a pool

Industry/Entity Type

Pool Service

Number of Pages Required

5+ page

Font styles to use
Serif

Colors
0455a3
3276b5
85acd3
85cae6
ffffff
33a6d7
0592cd

Requirements
Must have
• The Home page must have this picture highlighted in the top of the page:
• http://www.mesawaterpro.example/
• Must have pictures of some high-end pools. Any that you can find on the internet are wonderful.
• Must have a table on the right of the home page that mentions the service areas that we go to:
• • Carmel Valley (92130)
• • Del Mar (92014)
• • Rancho Santa Fe (92067)
• • Solana Beach (92075)
• • Santaluz (92127)
• • Cardiff (92007)
• • Encinitas (92024)
• • Carlsbad (92009, 92008)
• • La Jolla (92037)
• • Pacific Beach (92109)
• • Mira Mesa (92126)
• • Sorrento Valley (92121)
• • Clairemont (92117)
• • Rancho Bernardo (92127, 92128)
• • Rancho Penasquitos (92129)
• • Poway (92064)
• •
Nice to have
• Maybe incorporate some pictures of some kids (or families) playing in pools on the Why Hire Us page?
• I also like the feel of this website, but posting this page just for reference so you can get a feel more of what I like:
• http://www.crestlinepool.example/
• I like the FAQ's page from this website. I like how you can click on the question and then it pops up with the answer. http://www.dunewoodpoolcare.example/pool-spa-fountain-faqs/

```html
<!DOCTYPE html>
<html lang="en">
<head>
<meta charset="utf-8">
<title>Glimmerwave Pool Service</title>
<link href="https://fonts.googleapis.com/css2?family=Lato:ital,wght@0,400;0,700;1,400&display=swap" rel="stylesheet">
<style>
:root{
  --brand:#33a6d7;
  --brand-deep:#0592cd;
  --bar:#06a3d6;
  --ink:#555;
  --ink-dark:#333;
  --rule:#d9d9d9;
  --panel:#eeeeee;
  --footer:#141414;
  --white:#fff;
}
*{margin:0;padding:0;box-sizing:border-box}
html,body{width:713px;height:1200px;overflow:hidden;background:var(--white)}
body{position:relative;font-family:'Lato',Arial,sans-serif;color:var(--ink)}
.abs{position:absolute}
.site-header{left:0;top:0;width:713px;height:45px;background:linear-gradient(#fff,#e9e9e9);border-bottom:1px solid #ccc}
.brand-name{left:110px;top:11px;font-size:17px;font-weight:700;color:var(--brand);letter-spacing:.2px}
.main-nav{right:50px;top:18px;display:flex;gap:16px;font-size:7px;color:var(--ink-dark)}
.hero{left:0;top:45px;width:713px;height:272px;background:linear-gradient(180deg,#b9b5b8 0%,#7fb3cd 14%,#3bb4dc 32%,#1ca8da 62%,#0f92c8 100%)}
.hero-tagline{left:0;top:60px;width:713px;padding-left:80px;text-align:center;font-size:20px;font-weight:400;color:var(--white)}
.why-photo{left:110px;top:341px;width:136px;height:129px;border-radius:3px;background:linear-gradient(160deg,#7ed0ee,#2aa0d6 60%,#1a84c0)}
.section-title{font-size:14px;color:var(--brand);font-weight:400}
.why-title{left:257px;top:340px}
.why-rule{left:257px;top:359px;width:178px;height:1px;background:var(--rule)}
.why-text{left:258px;top:364px;width:343px;font-size:6.1px;line-height:12px;color:#666}
.divider{left:109px;top:489px;width:500px;height:1px;background:var(--rule)}
.column{top:499px;width:136px}
.col-rule{margin-top:3px;height:2px;width:136px;background:linear-gradient(90deg,var(--brand) 0 28px,#e2eef4 28px)}
.col-list{list-style:none;margin-top:7px;font-size:6.3px;line-height:13.4px;color:var(--ink-dark)}
.col-list li::before{content:"»";margin-right:5px}
.area-list li::before{content:"➞";margin-right:7px}
.col-text{margin-top:7px;font-size:6.2px;line-height:12.3px;color:#666}
.read-more{display:block;margin-top:4px;font-size:6.5px;color:var(--brand-deep)}
.testimonial{left:0;top:657px;width:713px;height:219px;background:linear-gradient(180deg,#2d3a40 0%,#12323f 45%,#0c2a35 100%)}
.testimonial-title{left:0;top:670px;width:713px;text-align:center;font-size:15px;font-weight:400;color:var(--white)}
.quote-badge{left:340px;top:714px}
.quote-text{left:118px;top:758px;width:477px;text-align:center;font-style:italic;font-size:9.2px;line-height:18px;color:var(--white)}
.quote-name{left:0;top:820px;width:713px;text-align:center;font-size:9px;color:var(--brand)}
.quote-role{left:0;top:833px;width:713px;text-align:center;font-size:7px;color:var(--brand)}
.dots{left:343px;top:858px;display:flex;gap:2px}
.dots span{width:5px;height:5px;border-radius:50%;background:var(--white)}
.faq-title{left:0;top:888px;width:713px;text-align:center;font-size:12px;font-weight:400;color:var(--brand)}
.faq{left:151px;top:915px;width:411px}
.faq-q{height:23px;background:var(--bar);color:var(--white);font-size:8.5px;display:flex;align-items:center;justify-content:space-between;padding:0 10px 0 12px;border-bottom:1px solid #3bb6e0}
.faq-a{background:var(--panel);font-size:6.1px;line-height:11px;color:#777;padding:8px 12px 9px}
.site-footer{left:0;top:1111px;width:713px;height:89px;background:var(--footer)}
.contact-row{left:0;top:1127px;width:713px;display:flex;justify-content:center;align-items:center;gap:18px;color:var(--white)}
.contact-item{display:flex;align-items:center;gap:10px}
.contact-email{font-size:8.5px}
.contact-phone{font-size:12.5px}
.contact-sep{width:1px;height:20px;background:#444}
.footer-rule{left:139px;top:1153px;width:432px;height:1px;background:#333}
.legal{left:0;top:1162px;width:713px;text-align:center;font-size:6.2px;line-height:13px;color:#ddd}
</style>
</head>
<body>
<header class="abs site-header">
  <div class="abs brand-name">Glimmerwave Pool Service</div>
  <nav class="abs main-nav"><span>Home</span><span>About Us</span><span>Services Offered</span><span>FAQ's</span><span>Why Hire Us</span><span>Contact</span></nav>
</header>

<div class="abs hero" role="img" aria-label="Infinity pool with clear blue water overlooking the sea and a white terrace"></div>
<h1 class="abs hero-tagline">Water so pure, it sparkles like a summer sky.</h1>

<div class="abs why-photo" role="img" aria-label="Children with swim goggles smiling in a pool"></div>
<h2 class="abs section-title why-title">Why You Need Us</h2>
<div class="abs why-rule"></div>
<p class="abs why-text">A swimming pool is a major investment, and pool care is a chore that cannot be neglected. An improperly maintained pool will eventually damage your pool's surface and equipment, costing you thousands of dollars to repair or replace. Many pool owners are unaware that incorrect pool chemistry can turn pool water into a severe health hazard and can possibly make you ill. While we always take care to keep your pool spotless and beautiful, we also clean up what you can't see. Our focus on and specialized knowledge of water health and safety prevents the growth of dangerous micro-organisms and bacteria that can make your family and guests seriously ill. The bottom line is that there's a lot more to pool care than debris removal. Be sure that the person who takes care of your pool knows what they're doing! As Certified Water Technicians, our technicians have undergone a course of instruction in pool health and safety sanctioned by the National Aquatic Care Institute. We'll keep your pool clean, healthy, and safe for you</p>
<div class="abs divider"></div>

<section class="abs column" style="left:109px">
  <h2 class="section-title">Our Services</h2><div class="col-rule"></div>
  <ul class="col-list">
    <li>Swimming Pool and Spa Cleaning</li><li>Install and repair lighting</li><li>New Pool and Spa Start Ups</li><li>Leak Detection Salt System Conversions</li><li>Troubleshoot and Repair pumps, filters,</li><li>Fountain Cleaning and Service</li><li>Tile Cleaning &amp; Restoration</li>
  </ul>
  <a class="read-more">Read More ⟶</a>
</section>
<section class="abs column" style="left:278px;width:156px">
  <h2 class="section-title">Our Mission</h2><div class="col-rule"></div>
  <p class="col-text">At Glimmerwave Pool Service, we understand that your pool is an important investment. Whether it's part of your business or in your backyard, it needs to be well taken care of to ensure its longevity and your peace of mind. At Glimmerwave Pool Service, we pride ourselves in setting the standard in our industry. What sets us apart from our competition</p>
  <a class="read-more" style="margin-top:10px">Read More ⟶</a>
</section>
<section class="abs column" style="left:447px">
  <h2 class="section-title">Service Area</h2><div class="col-rule"></div>
  <ul class="col-list area-list" style="line-height:12.4px;margin-top:6px">
    <li>Carmel Valley (92130)</li><li>Del Mar (92014)</li><li>Rancho Santa Fe (92067)</li><li>Solana Beach (92075)</li><li>Santaluz (92127)</li><li>Cardiff (92007)</li><li>Encinitas (92024)</li>
  </ul>
  <a class="read-more" style="margin-top:7px">Read More ⟶</a>
</section>

<section class="abs testimonial" role="img" aria-label="Darkened view of the infinity pool and terrace"></section>
<h2 class="abs testimonial-title">Testimonial</h2>
<svg class="abs quote-badge" width="33" height="33" viewBox="0 0 33 33" aria-hidden="true">
  <circle cx="16.5" cy="16.5" r="16.5" fill="#0aa6dc"/>
  <path d="M9 14h6v6h-5v-6c0-3 2-5 4-5v2c-1 0-2 1-2 3zM18 14h6v6h-5v-6c0-3 2-5 4-5v2c-1 0-2 1-2 3z" fill="#fff"/>
</svg>
<p class="abs quote-text">Working with Eli is terrific. His education and professional background sets him apart from all the other pool cleaners. He has excellent communication with us and he shows up when he says he will. Glimmerwave is the only pool care company I have ever recommended to my friends.</p>
<div class="abs quote-name">Dana Whitfield</div>
<div class="abs quote-role">Client</div>
<div class="abs dots"><span></span><span></span><span></span><span></span></div>

<h2 class="abs faq-title">Frequently Asked Questions</h2>
<div class="abs faq">
  <div class="faq-q">Why do my pool and spa need to be chlorinated?<svg width="11" height="11" viewBox="0 0 11 11"><rect width="11" height="11" rx="2" fill="#fff"/><path d="M5.5 2.5v6M2.5 5.5h6" stroke="#06a3d6" stroke-width="1.6"/></svg></div>
  <div class="faq-a">Pools should be disinfected continuously by a chemical which imparts a residual effect. Chlorine is a type of "disinfectant", also called a "sanitizer". Disinfects or sanitizers destroy living microorganisms and bacteria, preventing the transmission of disease. There are several types of disinfectants, such as chlorine, bromine, salt chlorination, ozone, and UV light. Pools need a disinfectant with a measurable residual.</div>
  <div class="faq-q" style="margin-top:4px">Why do my pool and spa need to be chlorinated?<svg width="11" height="11" viewBox="0 0 11 11"><rect width="11" height="11" rx="2" fill="#fff"/><path d="M2.5 5.5h6" stroke="#06a3d6" stroke-width="1.6"/></svg></div>
  <div class="faq-q">Why do my pool and spa need to be chlorinated?<svg width="11" height="11" viewBox="0 0 11 11"><rect width="11" height="11" rx="2" fill="#fff"/><path d="M2.5 5.5h6" stroke="#06a3d6" stroke-width="1.6"/></svg></div>
  <div class="faq-q">Why do my pool and spa need to be chlorinated?<svg width="11" height="11" viewBox="0 0 11 11"><rect width="11" height="11" rx="2" fill="#fff"/><path d="M2.5 5.5h6" stroke="#06a3d6" stroke-width="1.6"/></svg></div>
  <div class="faq-q">Why do my pool and spa need to be chlorinated?<svg width="11" height="11" viewBox="0 0 11 11"><rect width="11" height="11" rx="2" fill="#fff"/><path d="M2.5 5.5h6" stroke="#06a3d6" stroke-width="1.6"/></svg></div>
</div>

<footer class="abs site-footer"></footer>
<div class="abs contact-row">
  <div class="contact-item">
    <svg width="20" height="15" viewBox="0 0 20 15" aria-hidden="true"><rect width="20" height="15" rx="1.5" fill="#fff"/><path d="M1 1.5l9 7 9-7" fill="none" stroke="#141414" stroke-width="1.4"/></svg>
    <span class="contact-email">info@glimmerwavepool.example</span>
  </div>
  <div class="contact-sep"></div>
  <div class="contact-item">
    <svg width="15" height="15" viewBox="0 0 24 24" aria-hidden="true"><path d="M6.6 10.8a15 15 0 0 0 6.6 6.6l2.2-2.2a1 1 0 0 1 1-.25 11.4 11.4 0 0 0 3.6.57 1 1 0 0 1 1 1V20a1 1 0 0 1-1 1A17 17 0 0 1 3 4a1 1 0 0 1 1-1h3.5a1 1 0 0 1 1 1c0 1.25.2 2.45.57 3.57a1 1 0 0 1-.25 1z" fill="#fff"/></svg>
    <span class="contact-phone">(858) 555-0142</span>
  </div>
</div>
<div class="abs footer-rule"></div>
<p class="abs legal">LA &amp; San Fernando Valley Swimming Pool Service © 1995-2015 Harborline Pool Service. All Rights Reserved<br>4820 Coral Tide Ave. / Suite 210 / Sherman Oaks, CA 91400</p>
</body>
</html>
```